Laundry Service Description Tri-Fold Brochure

My laundry business offers a service called "Velnora - Wet Cleaning"
I am after a design for a tri fold brochure to hand out to my customers. This will detail the benefits of wet cleaning vs dry cleaning.
I want the brochure to highlight the customer benefits NOT the business benefits.
I have attached the logo of our laundry which should be included
A couple of links here for more information and pdfs are attached:
https://brindlepartsupplyhub.com.au/laundry/velnora-wet-cleaning.html
https://www.quorv.co.za/wet-cleaning/
I have attached the design of our laundry window and ideally i want the brochure designed similar

```html
<!DOCTYPE html>
<html lang="en">
<head>
<meta charset="utf-8">
<title>Calloway Laundry Services – Tri-Fold Brochure</title>
<link href="https://fonts.googleapis.com/css2?family=Montserrat:wght@400;500;600;700&family=Open+Sans:wght@400;600;700&display=swap" rel="stylesheet">
<style>
:root{
  --navy:#123b80;
  --blue:#1d5eb0;
  --mid:#2f86cf;
  --sky:#58bde9;
  --pale:#bfe7f8;
  --ice:#e9f7fd;
  --white:#ffffff;
  --stage:#e4e6e8;
  --ink:#1b3e6e;
}
*{box-sizing:border-box;margin:0;padding:0}
html,body{width:1200px;height:2400px;overflow:hidden}
body{background:var(--stage);font-family:"Open Sans",Arial,sans-serif;position:relative}
.sheet{position:absolute;left:30px;width:1140px;height:880px;display:flex;box-shadow:0 8px 30px rgba(0,0,0,.18);background:var(--white)}
.sheet--outside{top:200px}
.sheet--inside{top:1300px}
.panel{position:relative;width:380px;height:880px;overflow:hidden}
.panel + .panel{border-left:1px solid rgba(0,0,0,.06)}
.photo{position:absolute}
.curve{position:absolute;left:0;width:380px}
.heading{font-family:"Montserrat",Arial,sans-serif;font-weight:700;letter-spacing:.5px;text-transform:uppercase}
.body-text{font-size:13px;line-height:1.6}
.pill{position:absolute;left:30px;right:30px;height:38px;border-radius:19px;display:flex;align-items:center;justify-content:center;font-family:"Montserrat",Arial,sans-serif;font-weight:600;font-size:14px}
.brand{font-family:"Montserrat",Arial,sans-serif;font-weight:600;display:flex;align-items:center;gap:10px}
.brand__dot{width:14px;height:14px;border-radius:50%;flex:none}
.bullets{list-style:none}
.bullets li{position:relative;padding-left:18px;font-size:13px;line-height:1.5;margin-bottom:6px}
.bullets li::before{content:"";position:absolute;left:0;top:6px;width:8px;height:8px;border-radius:50%;background:currentColor;opacity:.85}

/* outside: about */
.about{background:var(--navy);color:var(--white)}
.about .photo{top:0;left:0;width:380px;height:300px;background:linear-gradient(160deg,#9fd9f2,#e7c9bb 55%,#6cc3ea)}
.about .curve{top:220px}
.about__content{position:absolute;top:340px;left:32px;right:32px}
.about__content .heading{font-size:18px;margin-bottom:14px}
.about__content .body-text{margin-bottom:12px;color:#dbe9fb}
.about .pill{bottom:34px;background:var(--mid);color:var(--white)}

/* outside: contact */
.contact{background:var(--white);color:var(--ink)}
.contact .photo{top:40px;left:100px;width:180px;height:180px;border-radius:50%;border:8px solid var(--sky);background:linear-gradient(180deg,#cfe4f6,#6f9fd4 60%,#f1f5fb)}
.contact__content{position:absolute;top:260px;left:30px;right:30px;text-align:center}
.contact .brand{justify-content:center;font-size:30px;color:var(--blue);margin-bottom:10px}
.contact__tag{font-family:"Montserrat",Arial,sans-serif;font-weight:700;color:var(--mid);font-size:17px}
.contact__sub{font-family:"Montserrat",Arial,sans-serif;color:var(--mid);font-size:16px;margin:4px 0 16px}
.contact .body-text{color:#44607f;margin-bottom:22px}
.contact__cta{font-family:"Montserrat",Arial,sans-serif;font-weight:700;color:var(--blue);font-size:17px;margin-bottom:12px}
.contact .pill{position:relative;left:auto;right:auto;margin:0 20px 12px;background:var(--pale);color:var(--blue);font-size:20px}
.contact__web{font-family:"Montserrat",Arial,sans-serif;font-weight:600;color:var(--blue);font-size:15px}
.contact .curve{bottom:0}

/* outside: cover */
.cover{background:var(--navy);color:var(--white)}
.cover .photo{top:0;left:0;width:380px;height:560px;background:linear-gradient(160deg,#8fd6f3,#c9e9f6 40%,#d89c78 62%,#8ad0ee)}
.cover .curve{top:430px}
.cover__content{position:absolute;top:600px;left:30px;right:30px;text-align:center}
.cover .brand{justify-content:center;font-size:36px;margin-bottom:14px}
.cover__tag{font-family:"Montserrat",Arial,sans-serif;font-weight:700;font-size:19px;letter-spacing:.5px}
.cover__sub{font-family:"Montserrat",Arial,sans-serif;font-size:17px;color:var(--pale);margin-top:6px}
.cover .pill{bottom:40px;background:var(--sky);color:var(--white)}

/* inside: benefits */
.inside-bg{background:linear-gradient(180deg,#3ea6de,#64c2ec);color:var(--white)}
.benefits__content,.dry__content{position:absolute;top:40px;left:30px;right:30px}
.benefits__content .heading,.dry__content .heading{font-size:18px;margin-bottom:14px;display:flex;align-items:center;gap:10px}
.benefits__content .body-text,.dry__content .body-text{margin-bottom:16px}
.benefits .photo{left:0;bottom:0;width:380px;height:250px;background:linear-gradient(150deg,#f0ede8,#a9c7e4 50%,#e8d8cc)}
.benefits .curve{bottom:170px}
.heading-icon{width:26px;height:26px;border-radius:50%;background:var(--white);flex:none;display:flex;align-items:center;justify-content:center}

/* inside: dry */
.dry__base{position:absolute;left:0;bottom:0;width:380px;height:240px;background:var(--navy)}
.dry .curve{bottom:180px}
.dry .photo{right:36px;bottom:150px;width:130px;height:130px;border-radius:50%;border:6px solid var(--white);background:linear-gradient(180deg,#cfe2f5,#2f6fc0 55%,#f0c64a)}
.dry .brand{position:absolute;left:30px;bottom:60px;font-size:30px;color:var(--white)}
.dry__web{position:absolute;left:30px;bottom:34px;font-family:"Montserrat",Arial,sans-serif;font-size:13px;color:var(--pale)}

/* inside: compare */
.compare{background:var(--white);color:var(--ink)}
.compare .photo{top:0;left:0;width:380px;height:290px;background:linear-gradient(160deg,#dde9f5,#f3e2cf 45%,#9fc6e6)}
.compare .curve{top:220px}
.compare__table{position:absolute;top:320px;left:22px;right:22px;display:grid;grid-template-columns:1fr 1fr;gap:10px}
.compare__col{background:var(--ice);border-radius:10px;padding:12px 10px}
.compare__head{display:flex;flex-direction:column;align-items:center;gap:6px;font-family:"Montserrat",Arial,sans-serif;font-weight:700;font-size:13px;color:var(--blue);margin-bottom:10px}
.compare__badge{width:40px;height:40px;border-radius:50%;background:var(--sky);display:flex;align-items:center;justify-content:center}
.compare__row{display:flex;flex-direction:column;align-items:center;text-align:center;gap:5px;padding:10px 0;border-top:1px solid var(--pale);font-size:12px;color:#3d5f86}
.compare__row svg{display:block}
</style>
</head>
<body>

<section class="sheet sheet--outside">
  <article class="panel about">
    <div class="photo" role="img" aria-label="Photo of a smiling woman holding a stack of folded towels"></div>
    <svg class="curve" viewBox="0 0 380 120" height="120" aria-hidden="true">
      <path d="M0 50 Q190 150 380 20 L380 120 L0 120Z" fill="var(--navy)"/>
      <path d="M0 40 Q190 140 380 10" fill="none" stroke="var(--sky)" stroke-width="8"/>
    </svg>
    <div class="about__content">
      <h2 class="heading">About Us</h2>
      <p class="body-text">Since opening our doors, we have cared for the clothes of families and businesses across the island. Our trained team treats every garment as if it were our own, using gentle water based methods and modern equipment.</p>
      <p class="body-text">We collect, clean and return your items on time, with care you can feel in every fold.</p>
    </div>
    <div class="pill">www.callowaylaundry.com.cy</div>
  </article>

  <article class="panel contact">
    <div class="photo" role="img" aria-label="Photo of a neat stack of folded shirts"></div>
    <div class="contact__content">
      <div class="brand"><span class="brand__dot" style="background:var(--sky)"></span>Calloway Laundry Services</div>
      <p class="contact__tag">VELNORA • WET CLEANING</p>
      <p class="contact__sub">We are passionate about laundry!</p>
      <p class="body-text">We are professionals in the laundry and cleaning business and we take pride in giving you fresh, soft and safely cleaned clothes every time you visit.</p>
      <p class="contact__cta">CONTACT US TODAY!</p>
      <div class="pill">
        <svg width="18" height="18" viewBox="0 0 24 24" aria-hidden="true" style="margin-right:8px"><path d="M6.6 10.8a15 15 0 0 0 6.6 6.6l2.2-2.2a1 1 0 0 1 1-.25 11.4 11.4 0 0 0 3.6.57 1 1 0 0 1 1 1V20a1 1 0 0 1-1 1A17 17 0 0 1 3 4a1 1 0 0 1 1-1h3.5a1 1 0 0 1 1 1c0 1.25.2 2.45.57 3.6a1 1 0 0 1-.25 1z" fill="var(--blue)"/></svg>
        +357 23 555 014
      </div>
      <p class="contact__web">www.callowaylaundry.com.cy</p>
    </div>
    <svg class="curve" viewBox="0 0 380 80" height="80" aria-hidden="true">
      <path d="M0 40 Q200 90 380 10 L380 80 L0 80Z" fill="var(--pale)"/>
    </svg>
  </article>

  <article class="panel cover">
    <div class="photo" role="img" aria-label="Photo of a cheerful bearded man in an apron holding an armful of laundry"></div>
    <svg class="curve" viewBox="0 0 380 160" height="160" aria-hidden="true">
      <path d="M0 90 Q120 150 380 20 L380 160 L0 160Z" fill="var(--navy)"/>
      <path d="M0 70 Q120 130 380 0" fill="none" stroke="var(--sky)" stroke-width="10"/>
      <path d="M0 86 Q120 146 380 16" fill="none" stroke="var(--white)" stroke-width="4"/>
    </svg>
    <div class="cover__content">
      <div class="brand"><span class="brand__dot" style="background:var(--sky)"></span>Calloway Laundry Services</div>
      <p class="cover__tag">VELNORA • WET CLEANING</p>
      <p class="cover__sub">We are passionate about laundry!</p>
    </div>
    <div class="pill">www.callowaylaundry.com.cy</div>
  </article>
</section>

<section class="sheet sheet--inside">
  <article class="panel benefits inside-bg">
    <div class="benefits__content">
      <h2 class="heading">Benefits of Wet Cleaning</h2>
      <p class="body-text">Wet cleaning is a gentle, modern way to clean garments that were once sent only to dry cleaners. It uses water, mild detergents and careful machines instead of harsh solvents.</p>
      <ul class="bullets">
        <li>No chemical smell left on your clothes</li>
        <li>Brighter colours and softer fabrics</li>
        <li>Safe for sensitive skin and allergies</li>
        <li>Removes water based stains more easily</li>
        <li>Kind to delicate silks and wools</li>
        <li>Better for your home and the planet</li>
      </ul>
    </div>
    <div class="photo" role="img" aria-label="Photo of two laundry staff checking a garment together"></div>
    <svg class="curve" viewBox="0 0 380 120" height="120" aria-hidden="true">
      <path d="M0 0 L380 0 L380 40 Q180 120 0 60Z" fill="#5fc0eb"/>
      <path d="M0 60 Q180 120 380 40" fill="none" stroke="var(--white)" stroke-width="8"/>
    </svg>
  </article>

  <article class="panel dry inside-bg">
    <div class="dry__content">
      <h2 class="heading"><span class="heading-icon"><svg width="14" height="14" viewBox="0 0 24 24" aria-hidden="true"><path d="M12 2C9 7 5 10 5 15a7 7 0 0 0 14 0c0-5-4-8-7-13z" fill="var(--mid)"/></svg></span>Dry Cleaning</h2>
      <p class="body-text">Dry cleaning uses chemical solvents rather than water. These solvents can stay in fabric and may affect how your clothes look, feel and smell over time.</p>
      <ul class="bullets">
        <li>Solvent odours can linger after pickup</li>
        <li>Whites may turn grey or yellow</li>
        <li>Fabrics can feel stiff or dry</li>
        <li>Some stains set instead of lifting</li>
        <li>Harsh on skin for some people</li>
      </ul>
    </div>
    <div class="dry__base"></div>
    <svg class="curve" viewBox="0 0 380 100" height="100" aria-hidden="true">
      <path d="M0 30 Q200 110 380 40 L380 100 L0 100Z" fill="var(--navy)"/>
      <path d="M0 30 Q200 110 380 40" fill="none" stroke="var(--white)" stroke-width="6"/>
    </svg>
    <div class="photo" role="img" aria-label="Photo of folded blue shirts in a basket"></div>
    <div class="brand"><span class="brand__dot" style="background:var(--sky)"></span>Calloway</div>
    <p class="dry__web">www.callowaylaundry.com.cy</p>
  </article>

  <article class="panel compare">
    <div class="photo" role="img" aria-label="Photo of a laundry attendant handing a wrapped garment to a customer"></div>
    <svg class="curve" viewBox="0 0 380 100" height="100" aria-hidden="true">
      <path d="M0 60 Q200 120 380 20 L380 100 L0 100Z" fill="var(--white)"/>
      <path d="M0 52 Q200 112 380 12" fill="none" stroke="var(--sky)" stroke-width="8"/>
    </svg>
    <div class="compare__table">
      <div class="compare__col">
        <div class="compare__head"><span class="compare__badge"><svg width="20" height="20" viewBox="0 0 24 24" aria-hidden="true"><path d="M12 2C9 7 5 10 5 15a7 7 0 0 0 14 0c0-5-4-8-7-13z" fill="#fff"/></svg></span>WET CLEANING</div>
        <div class="compare__row"><svg width="22" height="22" viewBox="0 0 24 24" aria-hidden="true"><path d="M5 12l4 4 10-10" fill="none" stroke="var(--mid)" stroke-width="3"/></svg>Gentle on fabrics</div>
        <div class="compare__row"><svg width="22" height="22" viewBox="0 0 24 24" aria-hidden="true"><path d="M5 12l4 4 10-10" fill="none" stroke="var(--mid)" stroke-width="3"/></svg>No chemical odour</div>
        <div class="compare__row"><svg width="22" height="22" viewBox="0 0 24 24" aria-hidden="true"><path d="M5 12l4 4 10-10" fill="none" stroke="var(--mid)" stroke-width="3"/></svg>Safe for skin</div>
        <div class="compare__row"><svg width="22" height="22" viewBox="0 0 24 24" aria-hidden="true"><path d="M5 12l4 4 10-10" fill="none" stroke="var(--mid)" stroke-width="3"/></svg>Fresh, bright colours</div>
      </div>
      <div class="compare__col">
        <div class="compare__head"><span class="compare__badge" style="background:var(--blue)"><svg width="20" height="20" viewBox="0 0 24 24" aria-hidden="true"><circle cx="12" cy="12" r="7" fill="none" stroke="#fff" stroke-width="3"/></svg></span>DRY CLEANING</div>
        <div class="compare__row"><svg width="22" height="22" viewBox="0 0 24 24" aria-hidden="true"><path d="M6 6l12 12M18 6L6 18" stroke="var(--blue)" stroke-width="3"/></svg>Harsh solvents</div>
        <div class="compare__row"><svg width="22" height="22" viewBox="0 0 24 24" aria-hidden="true"><path d="M6 6l12 12M18 6L6 18" stroke="var(--blue)" stroke-width="3"/></svg>Lingering smell</div>
        <div class="compare__row"><svg width="22" height="22" viewBox="0 0 24 24" aria-hidden="true"><path d="M6 6l12 12M18 6L6 18" stroke="var(--blue)" stroke-width="3"/></svg>May irritate skin</div>
        <div class="compare__row"><svg width="22" height="22" viewBox="0 0 24 24" aria-hidden="true"><path d="M6 6l12 12M18 6L6 18" stroke="var(--blue)" stroke-width="3"/></svg>Colours can dull</div>
      </div>
    </div>
  </article>
</section>

</body>
</html>
```